Option Sheet

We need a one page option sheet with a left to right reading of the five options. It should be a one sheet, multiple colors and definitive separations between options This is used in a sales consultation. Backround or colors not in option need to have the follow RGB value (5 red, 20 green, 63 blue)

We added a smaller text file, please change that point

Target Market(s)

Divorce

Industry/Entity Type

Legal

Requirements
Must have
• 1) All five options left to right
• 2)language included in sheet

```html
<!DOCTYPE html>
<html lang="en">
<head>
<meta charset="utf-8">
<title>Five Options Divorce – Option Sheet</title>
<link rel="stylesheet" href="https://fonts.googleapis.com/css2?family=Archivo+Black&family=Arimo:ital,wght@0,400;0,700;1,700&display=swap">
<style>
  :root {
    --navy: rgb(14, 21, 58);
    --ink: #15182b;
    --white: #ffffff;
    --rule: rgba(255, 255, 255, .85);
    --blue: #7fd3f5;
    --pink: #f287b4;
    --yellow: #fdf16d;
    --green: #9cca8b;
    --orange: #fbbf7e;
  }
  * { margin: 0; padding: 0; box-sizing: border-box; }
  html, body { width: 1200px; height: 848px; overflow: hidden; background: var(--navy); }
  .sheet { position: relative; width: 1200px; height: 848px; background: var(--navy); font-family: "Arimo", Arial, sans-serif; color: var(--ink); }

  .notched {
    --r: 16px;
    background:
      radial-gradient(circle at 0 0, transparent var(--r), var(--c) calc(var(--r) + 1px)) top left,
      radial-gradient(circle at 100% 0, transparent var(--r), var(--c) calc(var(--r) + 1px)) top right,
      radial-gradient(circle at 0 100%, transparent var(--r), var(--c) calc(var(--r) + 1px)) bottom left,
      radial-gradient(circle at 100% 100%, transparent var(--r), var(--c) calc(var(--r) + 1px)) bottom right;
    background-size: 51% 51%;
    background-repeat: no-repeat;
  }

  .title-banner { position: absolute; left: 33px; top: 42px; width: 1130px; height: 92px; --c: var(--white); display: flex; align-items: center; justify-content: center; }
  .title-banner h1 { font-family: "Archivo Black", "Arial Black", sans-serif; font-size: 74px; letter-spacing: 1px; color: var(--navy); text-shadow: 3px 4px 4px rgba(0,0,0,.45); line-height: 1; margin-top: -6px; }

  .base-bar { position: absolute; left: 33px; top: 801px; width: 1130px; height: 20px; background: var(--white); }

  .markers { position: absolute; inset: 0; pointer-events: none; }
  .markers text { font-family: "Arimo", Arial, sans-serif; font-weight: 700; font-style: italic; font-size: 21px; fill: var(--navy); text-anchor: middle; }

  .option { position: absolute; top: 178px; height: 579px; padding: 16px 10px 0 22px; --r: 15px; }
  .option::before { content: ""; position: absolute; left: 22px; right: 22px; top: 16px; border-top: 1px solid var(--rule); }
  .opt-1 { left: 39px; width: 172px; --c: var(--blue); }
  .opt-2 { left: 230px; width: 200px; --c: var(--pink); }
  .opt-3 { left: 449px; width: 230px; --c: var(--yellow); }
  .opt-4 { left: 696px; width: 278px; --c: var(--green); }
  .opt-5 { left: 992px; width: 173px; --c: var(--orange); }

  .option h2 {
    font-weight: 700; font-size: 29px; line-height: 29px; letter-spacing: -0.6px;
    text-align: center; color: var(--ink); margin: 14px 0 8px -12px;
    text-shadow: 1px 0 0 #fff, -1px 0 0 #fff, 0 1px 0 #fff, 0 -1px 0 #fff, 2px 2px 2px rgba(0,0,0,.35);
  }
  .option h3 { font-weight: 700; font-style: italic; font-size: 18px; text-decoration: underline; margin: 4px 0 5px; text-shadow: 1px 1px 0 #fff; }
  .option ul { list-style: none; margin-bottom: 8px; }
  .option li { position: relative; padding-left: 19px; font-size: 17.5px; line-height: 22.3px; margin-bottom: 4px; }
  .option li::before { content: ""; position: absolute; left: 0; top: 5px; width: 10px; height: 10px; border: 2.5px solid var(--ink); border-radius: 50%; }

  .rules { position: absolute; left: 12px; right: 12px; bottom: 15px; display: flex; flex-direction: column; align-items: center; gap: 12.6px; }
  .rules.single { bottom: 24px; }
  .rules span { display: block; height: 0; border-top: 1px solid var(--rule); }
</style>
</head>
<body>
<main class="sheet">
  <header class="title-banner notched"><h1>Five Options Divorce</h1></header>

  <section class="option opt-1 notched">
    <h2>Do Nothing</h2>
    <h3>Advantages:</h3>
    <ul>
      <li>Stay married</li>
      <li>No life<br>Changes</li>
    </ul>
    <h3>Disadvantages:</h3>
    <ul>
      <li>Remain<br>unhappy,<br>depressed,<br>anxious</li>
      <li>Money and<br>assets may<br>disappear</li>
      <li>What is<br>going to<br>change?</li>
    </ul>
    <div class="rules"><span style="width:150px"></span><span style="width:138px"></span><span style="width:130px"></span><span style="width:122px"></span><span style="width:114px"></span><span style="width:104px"></span><span style="width:96px"></span><span style="width:86px"></span><span style="width:76px"></span><span style="width:58px"></span></div>
  </section>

  <section class="option opt-2 notched">
    <h2>Go to<br>Counseling</h2>
    <h3>Advantages:</h3>
    <ul>
      <li>Reconcile<br>marriage</li>
      <li>Help make<br>a better life</li>
    </ul>
    <h3>Disadvantages:</h3>
    <ul>
      <li>Past issues are<br>highlighted and<br>may drudge up<br>old wounds</li>
      <li>It may just clarify<br>the reasons you<br>need to separate<br>and/or divorce</li>
      <li>Both parties<br>must be invested<br>and willing to<br>participate</li>
    </ul>
    <div class="rules"><span style="width:172px"></span><span style="width:162px"></span><span style="width:128px"></span></div>
  </section>

  <section class="option opt-3 notched">
    <h2>Do it Yourself</h2>
    <h3>Advantages:</h3>
    <ul>
      <li>No attorney fees</li>
      <li>You are your on<br>attorney</li>
    </ul>
    <h3>Disadvantages:</h3>
    <ul>
      <li>People often find<br>that what is “fair,”<br>may in fact, not be<br>truly fair</li>
      <li>Often times, people<br>do not know the<br>risks</li>
      <li>Complicated legal<br>system within<br>intrigue rules</li>
      <li>Unsure how<br>to complete<br>the necessary<br>paperwork and<br>meet the deadlines</li>
    </ul>
    <div class="rules single"><span style="width:186px"></span></div>
  </section>

  <section class="option opt-4 notched">
    <h2>Limited<br>Representation</h2>
    <h3>Advantages:</h3>
    <ul>
      <li>Balance between going<br>alone and our limited<br>involvement in the case</li>
    </ul>
    <h3>Disadvantages:</h3>
    <ul>
      <li>Our terms may not benefit<br>from our legal knowledge</li>
      <li>The legal consequences<br>of your legal documents<br>will not be explained<br>to you so that you can<br>formulate a plan for<br>handling the rest of your<br>case.</li>
      <li>Your spouse or other<br>parties may cause your<br>legal fees to increase<br>significantly without action<br>on your part</li>
    </ul>
    <div class="rules single"><span style="width:234px"></span></div>
  </section>

  <section class="option opt-5 notched">
    <h2>Hire Us</h2>
    <h3>Advantages:</h3>
    <ul>
      <li>Gain the<br>full benefits<br>of our<br>experience</li>
      <li>Have a team<br>of Family<br>Law focus<br>attorneys</li>
      <li>Often saves<br>you or makes<br>you money in<br>the long run</li>
      <li>Save you<br>time, energy<br>and stress</li>
    </ul>
    <h3>Disadvantages:</h3>
    <ul>
      <li>Initial cost</li>
    </ul>
    <div class="rules"><span style="width:138px"></span><span style="width:130px"></span><span style="width:120px"></span><span style="width:108px"></span><span style="width:94px"></span></div>
  </section>

  <div class="base-bar"></div>

  <svg class="markers" width="1200" height="848" viewBox="0 0 1200 848" aria-hidden="true">
    <g class="marker-top">
      <polygon points="92,134 160,134 126,178" fill="var(--blue)"/>
      <polygon points="296,134 364,134 330,178" fill="var(--pink)"/>
      <polygon points="530,134 598,134 564,178" fill="var(--yellow)"/>
      <polygon points="802,134 870,134 836,178" fill="var(--green)"/>
      <polygon points="1047,134 1115,134 1081,178" fill="var(--orange)"/>
      <text x="126" y="156">#1</text>
      <text x="330" y="156">#2</text>
      <text x="564" y="156">#3</text>
      <text x="836" y="156">#4</text>
      <text x="1081" y="156">#5</text>
    </g>
    <g class="marker-bottom">
      <polygon points="126,757 92,801 160,801" fill="var(--blue)"/>
      <polygon points="330,757 296,801 364,801" fill="var(--pink)"/>
      <polygon points="564,757 530,801 598,801" fill="var(--yellow)"/>
      <polygon points="836,757 802,801 870,801" fill="var(--green)"/>
      <polygon points="1081,757 1047,801 1115,801" fill="var(--orange)"/>
      <text x="126" y="795">#1</text>
      <text x="330" y="795">#2</text>
      <text x="564" y="795">#3</text>
      <text x="836" y="795">#4</text>
      <text x="1081" y="795">#5</text>
    </g>
  </svg>
</main>
</body>
</html>
```